Medical equipment business looking for professional, unique business card

We need a business card design for a durable medical equipment company. We are small but would like our cards to express that we are much bigger. We focus on braces (back, knee, wrist, etc) but also do crutches, rollators, wheelchairs- basically medical equipment that gets you going and back in Stride. Our colors are blue and green and our logo has an arrow and use of a "spine". We'd like to express professionalism while being unique.

Industry/Entity Type

Medical Equipment

Contact Information for Business Card

Professional feel but unique. Memorable.

Font styles to use
Serif
Sans Serif
Other font styles liked:
• verdana

Requirements
Must have
• card holders cell#, business phone#, fax#, email, website address, business address, logo
Nice to have
• use of medical/healthcare related descriptive words, items, look
Should not have
• the wrong colors or cartoon characters.

```html
<!DOCTYPE html>
<html lang="en">
<head>
<meta charset="utf-8">
<title>Stride Mobility – Business Card</title>
<link rel="stylesheet" href="https://fonts.googleapis.com/css2?family=Nunito:wght@400;600;700&display=swap">
<style>
  :root {
    --backdrop: #e9e6e1;
    --card-white: #fbfbfb;
    --navy: #0f4f7d;
    --navy-deep: #0a3d63;
    --lime: #8cc63f;
    --lime-soft: #b5dc72;
    --ink-blue: #1d4f7a;
    --text-light: #ffffff;
  }
  html, body {
    margin: 0;
    width: 1200px;
    height: 1022px;
    overflow: hidden;
    background: var(--backdrop);
    font-family: "Nunito", "Verdana", sans-serif;
  }
  .business-card {
    position: absolute;
    left: 150px;
    top: 254px;
    width: 900px;
    height: 514px;
    border-radius: 24px;
    overflow: hidden;
    background: var(--card-white);
    box-shadow: 0 12px 30px rgba(0,0,0,.18);
  }
  .card-art { position: absolute; inset: 0; }
  .brand {
    position: absolute;
    left: 70px;
    top: 190px;
    display: flex;
    align-items: center;
    gap: 14px;
  }
  .brand-dot {
    width: 22px; height: 22px;
    border-radius: 50%;
    background: var(--lime);
  }
  .brand-name {
    font-weight: 700;
    font-size: 46px;
    color: var(--ink-blue);
    letter-spacing: .5px;
  }
  .tagline {
    position: absolute;
    left: 72px;
    top: 272px;
    font-size: 21px;
    line-height: 1.35;
    color: var(--ink-blue);
    font-weight: 400;
  }
  .holder {
    position: absolute;
    left: 330px;
    top: 400px;
    color: var(--text-light);
  }
  .holder-name {
    font-weight: 700;
    font-size: 34px;
    color: var(--lime);
    line-height: 1.1;
  }
  .holder-title {
    font-size: 22px;
    margin-top: 4px;
  }
  .contact {
    position: absolute;
    right: 34px;
    top: 42px;
    display: grid;
    grid-template-columns: auto 22px;
    column-gap: 14px;
    row-gap: 2px;
    color: var(--text-light);
    font-size: 22px;
    line-height: 1.32;
    text-align: right;
    align-items: center;
  }
  .contact .icon { width: 16px; height: 16px; justify-self: center; }
  .contact .web-name { color: var(--lime); font-weight: 700; }
</style>
</head>
<body>
  <div class="business-card">
    <svg class="card-art" viewBox="0 0 900 514" width="900" height="514" aria-hidden="true">
      <defs>
        <linearGradient id="navyFill" x1="0" y1="0" x2="1" y2="1">
          <stop offset="0" stop-color="#175d8f"/>
          <stop offset="1" stop-color="#0a3d63"/>
        </linearGradient>
      </defs>
      <path d="M600 0 C480 20 500 210 360 330 C260 420 140 440 40 514 L900 514 L900 0 Z" fill="var(--lime-soft)"/>
      <path d="M625 0 C505 20 520 210 382 332 C282 420 160 444 62 514 L900 514 L900 0 Z" fill="var(--lime)"/>
      <path d="M652 0 C535 22 545 214 404 336 C304 424 184 448 86 514 L900 514 L900 0 Z" fill="url(#navyFill)"/>
      <circle cx="300" cy="514" r="34" fill="var(--lime)"/>
    </svg>

    <div class="brand">
      <span class="brand-dot"></span>
      <span class="brand-name">Stride Mobility</span>
    </div>
    <p class="tagline">Medical equipment that gets<br>you going and back in Stride</p>

    <div class="holder">
      <div class="holder-name">Marcus Ellery</div>
      <div class="holder-title">Director</div>
    </div>

    <div class="contact">
      <span>48 Harbor Lane Suite 210</span><span></span>
      <span>Lakeview, GA 30412</span><span></span>
      <span>+330 5180 2276</span>
      <svg class="icon" viewBox="0 0 16 16"><rect x="4" y="1" width="8" height="14" rx="1.5" fill="none" stroke="var(--lime)" stroke-width="1.6"/></svg>
      <span>+330 5180 4413</span>
      <svg class="icon" viewBox="0 0 16 16"><path d="M3 2 L6 2 L7 5 L5 6.5 C6 9 7 10 9.5 11 L11 9 L14 10 L14 13 C8 14 2 8 3 2 Z" fill="var(--lime)"/></svg>
      <span>+003 3419 6620</span>
      <svg class="icon" viewBox="0 0 16 16"><rect x="4" y="1" width="8" height="5" fill="var(--lime)"/><rect x="1" y="6" width="14" height="6" rx="1" fill="var(--lime)"/><rect x="4" y="10" width="8" height="5" fill="#ffffff"/></svg>
      <span>info@stridemobility.com</span>
      <svg class="icon" viewBox="0 0 16 16"><rect x="1" y="3" width="14" height="10" fill="none" stroke="var(--lime)" stroke-width="1.6"/><path d="M1 3 L8 9 L15 3" fill="none" stroke="var(--lime)" stroke-width="1.6"/></svg>
      <span>www.<span class="web-name">stridemobility</span>.com</span>
      <svg class="icon" viewBox="0 0 16 16"><circle cx="8" cy="8" r="6.5" fill="none" stroke="var(--lime)" stroke-width="1.6"/><path d="M1.5 8 H14.5 M8 1.5 C5 5 5 11 8 14.5 M8 1.5 C11 5 11 11 8 14.5" fill="none" stroke="var(--lime)" stroke-width="1.2"/></svg>
    </div>
  </div>
</body>
</html>
```